Educational Construction Organization needs Flyer for Upcoming Forum

We need a SAVE THE DATE Flyer for our 2020 Ravteq Forum. We work with Architects, Engineers, Contractors and Owners in the design and construction industry. Our mission is to evolve the capital projects industry through sharing of knowledge for optimized leadership, delivery and performance. The final design should communicate the connection between these industry professionals, our mission, and the Forum theme and byline.
Updates

Need extra days to review

Target Market(s)

Design and construction industry.

Industry/Entity Type

Construction

Font styles to use
Sans Serif

Colors

Designer to choose colors to be used in the design.

Requirements
Must have
• Title, By-line, 3 key topics, Date and location. Design that implements the theme with graphic(s) (not just text).
• NEW TITLE: FUTURE PROOFING: Connecting the dots to make sense of the "SMART" City
• 3 Key Topics: Smart Cities, Smart Institutions, Smart Connections
• Date: April 1-3, 2020
• Location: San Antonio, TX
Nice to have
• Please review attached problem statement for a better understanding of what this Forum will focus on when designing your graphic for the flyer.

```html
<!DOCTYPE html>
<html lang="en">
<head>
<meta charset="utf-8">
<title>2020 Ravteq Forum – Save the Date</title>
<link rel="stylesheet" href="https://fonts.googleapis.com/css2?family=Oswald:wght@500;600&family=Lato:ital,wght@0,400;0,700;1,700&display=swap">
<style>
:root{
  --navy:#1f2f8f;
  --blue:#2f5fc8;
  --sky:#3aa0dc;
  --sky-light:#7fd0f4;
  --green:#8bb33b;
  --green-dark:#79a02c;
  --ink:#1d2a5c;
  --body:#2b2f3a;
  --cyan-text:#2a9ad6;
  --bg:#ececee;
  --white:#ffffff;
}
*{box-sizing:border-box;margin:0;padding:0}
html,body{width:1200px;height:1200px;overflow:hidden}
body{background:var(--bg);position:relative;font-family:"Lato",sans-serif}
.page{position:absolute;top:183px;width:540px;height:766px;background:var(--white);overflow:hidden}
.page--front{left:39px}
.page--back{left:617px}
.abs{position:absolute}
.head-font{font-family:"Oswald",sans-serif;font-weight:500;text-transform:uppercase}

/* logo */
.brand{position:absolute;top:18px;display:flex;align-items:center;gap:10px}
.brand__dot{width:46px;height:46px;border-radius:50%;background:var(--navy)}
.brand__text{display:flex;flex-direction:column}
.brand__name{font-family:"Lato",sans-serif;font-weight:700;font-size:30px;color:var(--navy);line-height:1}
.brand__tag{font-size:7.5px;color:var(--green-dark);margin-top:4px;border-top:1px solid var(--navy);padding-top:3px}

/* front */
.save-tab{left:0;top:0}
.save-tab__text{left:14px;top:16px;font-size:30px;color:var(--white);letter-spacing:.3px;line-height:1.2}
.save-tab__text span{border-bottom:3px solid var(--green)}
.skyline{left:0;top:89px;width:540px;height:200px;background:linear-gradient(180deg,#4aa9e4 0%,#2f78cf 70%,#2244a8 100%)}
.date-band{left:0;top:270px;width:540px;height:72px}
.date-band__text{left:0;top:288px;width:540px;text-align:center;color:var(--white);font-size:40px;line-height:1.2;letter-spacing:.5px}
.location{left:0;top:342px;width:540px;height:35px;background:var(--green);display:flex;align-items:center;justify-content:center;gap:8px;color:var(--white);font-weight:700;font-size:17px}
.title{left:20px;top:412px;width:500px;font-size:35px;color:var(--navy);white-space:nowrap;line-height:1.2;text-align:justify;text-align-last:justify}
.title em{font-style:normal;color:var(--green)}
.title-rule{left:22px;top:462px;width:498px;border-top:3px dotted var(--green)}
.byline{left:19px;top:468px;font-size:17px;font-weight:700;color:var(--blue);white-space:nowrap}
.topics-tab{left:0;top:509px}
.topics-tab__text{left:22px;top:509px;font-size:22px;color:var(--white);line-height:32px}
.topic{position:absolute;top:557px;width:140px;text-align:center}
.topic__ring{width:98px;height:98px;margin:0 auto;border-radius:50%;border:3px dotted var(--green);padding:6px}
.topic__ring--blue{border-color:var(--sky)}
.topic__disc{width:100%;height:100%;border-radius:50%;background:var(--green)}
.topic__disc--blue{background:var(--sky)}
.topic__label{margin-top:10px;font-weight:700;font-size:14.5px;line-height:1.15;color:var(--navy)}
.topic-link{top:604px;height:0;border-top:4px dotted var(--navy)}
.footer-url{left:0;top:725px;width:540px;text-align:center;color:var(--white);font-weight:700;font-size:18px}

/* back */
.date-tab__text{right:10px;top:13px;font-size:33px;line-height:1.2;color:var(--white);white-space:nowrap}
.forum-strip{left:0;top:89px;width:540px;height:32px;background:var(--sky);color:var(--white);font-size:18px;text-align:center;line-height:32px;white-space:nowrap}
.network{left:0;top:121px;width:540px;height:168px;background:radial-gradient(ellipse at 60% 50%,#9fe3ff 0%,#3a9ae0 35%,#1e4fb8 75%,#1b3a9a 100%)}
.feature{position:absolute;width:86px;height:86px;border-radius:50%;border:4px solid #1e3f9c;background:var(--white);padding:6px}
.feature__disc{width:100%;height:100%;border-radius:50%;background:#d7e3f7}
.feature--green .feature__disc{background:var(--green)}
.feature--green{border-color:var(--white)}
.network-title{left:262px;top:166px;width:170px;font-size:26px;line-height:1.15;color:var(--navy);-webkit-text-stroke:1px var(--white);text-align:center;white-space:nowrap}
.byline-strip{left:0;top:289px;width:540px;height:53px;background:var(--navy);color:var(--white);font-size:16px;text-align:center;line-height:50px;border-top:2px solid var(--white);white-space:nowrap}
.copy{left:20px;top:359px;width:504px;font-size:12px;line-height:15.5px;color:var(--body)}
.copy p + p{margin-top:15.5px}
.copy .quote{color:var(--cyan-text);font-weight:700;font-style:italic}
</style>
</head>
<body>

<section class="page page--front" aria-label="Save the date flyer, front">
  <svg class="abs save-tab" width="540" height="80" aria-hidden="true">
    <defs><linearGradient id="tabFill" x1="0" x2="1"><stop offset="0" stop-color="#243a9e"/><stop offset="1" stop-color="#3b5cb8"/></linearGradient></defs>
    <rect width="540" height="4" fill="#5a8a4a"/>
    <polygon points="0,0 245,0 195,80 0,80" fill="url(#tabFill)"/>
  </svg>
  <div class="abs head-font save-tab__text"><span>Save the Date!</span></div>
  <div class="brand" style="left:330px">
    <div class="brand__dot"></div>
    <div class="brand__text">
      <span class="brand__name">I-Ravteq</span>
      <span class="brand__tag">Institute for Ravteq Capital Builders</span>
    </div>
  </div>

  <div class="abs skyline" role="img" aria-label="Blue city skyline illustration"></div>
  <svg class="abs date-band" width="540" height="72" viewBox="0 0 540 72" aria-hidden="true">
    <path d="M0,22 Q270,0 540,22 L540,72 L0,72 Z" fill="#2a45a8"/>
    <path d="M0,22 Q270,0 540,22" fill="none" stroke="#ffffff" stroke-width="3"/>
    <path d="M0,30 Q270,10 540,30" fill="none" stroke="#5b8ee0" stroke-width="2"/>
  </svg>
  <div class="abs head-font date-band__text">April 1-3, 2020</div>
  <div class="abs location">
    <svg width="16" height="22" viewBox="0 0 16 22" aria-hidden="true"><path d="M8 0C3.6 0 0 3.5 0 7.9 0 13.6 8 22 8 22s8-8.4 8-14.1C16 3.5 12.4 0 8 0zm0 11a3.2 3.2 0 1 1 0-6.4A3.2 3.2 0 0 1 8 11z" fill="#fff"/></svg>
    San Antonio, TX
  </div>

  <h1 class="abs head-font title">Making Sense of the <em>Smart City</em></h1>
  <div class="abs title-rule"></div>
  <p class="abs byline">Connecting the Dots for Dynamic Planning, Design and Delivery</p>

  <svg class="abs topics-tab" width="220" height="34" aria-hidden="true"><polygon points="0,0 172,0 148,34 0,34" fill="#2d4aa6"/></svg>
  <div class="abs head-font topics-tab__text">3 Key Topics:</div>

  <div class="abs topic-link" style="left:135px;width:80px"></div>
  <div class="abs topic-link" style="left:330px;width:80px"></div>
  <div class="topic" style="left:7px">
    <div class="topic__ring"><div class="topic__disc" role="img" aria-label="Smart cities icon"></div></div>
    <div class="topic__label">SMART<br>CITIES</div>
  </div>
  <div class="topic" style="left:203px">
    <div class="topic__ring topic__ring--blue"><div class="topic__disc topic__disc--blue" role="img" aria-label="Smart institutions icon"></div></div>
    <div class="topic__label">SMART<br>INSTITUTIONS</div>
  </div>
  <div class="topic" style="left:396px">
    <div class="topic__ring"><div class="topic__disc" role="img" aria-label="Smart connections icon"></div></div>
    <div class="topic__label">SMART<br>CONNECTIONS</div>
  </div>

  <svg class="abs" style="left:0;top:700px" width="540" height="66" aria-hidden="true"><ellipse cx="263" cy="100" rx="245" ry="90" fill="var(--green)"/></svg>
  <div class="abs footer-url">ravteqforum.org</div>
</section>

<section class="page page--back" aria-label="Save the date flyer, back">
  <svg class="abs" style="left:0;top:0" width="540" height="80" aria-hidden="true">
    <rect width="540" height="4" fill="var(--green)"/>
    <polygon points="296,0 540,0 540,80 346,80" fill="var(--green)"/>
  </svg>
  <div class="brand" style="left:32px">
    <div class="brand__dot"></div>
    <div class="brand__text">
      <span class="brand__name">I-Ravteq</span>
      <span class="brand__tag">Institute for Ravteq Capital Builders</span>
    </div>
  </div>
  <div class="abs head-font date-tab__text">April 1-3, 2020</div>

  <div class="abs head-font forum-strip">2020 Ravteq Capital Builders Forum</div>
  <div class="abs network" role="img" aria-label="Glowing blue network of connected dots"></div>
  <div class="feature" style="left:19px;top:138px"><div class="feature__disc" role="img" aria-label="Smart cities icon"></div></div>
  <div class="feature feature--green" style="left:117px;top:186px"><div class="feature__disc" role="img" aria-label="Smart institutions icon"></div></div>
  <div class="feature" style="left:447px;top:140px"><div class="feature__disc" role="img" aria-label="Smart connections icon"></div></div>
  <div class="abs head-font network-title">Making Sense of<br>the Smart City</div>
  <div class="abs head-font byline-strip">Connecting the Dots for Dynamic Planning, Design and Delivery</div>

  <div class="abs copy">
    <p>All over the nation, regions, cities and facility Owners are trying to get a handle on being “smart.” What does that mean for their piece of the built environment? Why should they care? Is it too late for them to get on board? Is this a justifiable investment or a waste of time, money and effort? Is being “smart” only focused on technologies? Who is coordinating all this stuff? Are cross-connections being made? It is obvious that a city provides different value to different stakeholders – depending on their needs in the moment – whether they are facility operators or planners, and whether or not that city is “smart,” at some point we all become end-users. We may not even consider our facilities or city as “smart,” but we experience them as places in which we work, play, live, visit. The Global Council of Urban Engineers (GCUE) envisions <span class="quote">a smart city as one that brings together technology, government, and society to enable the following characteristics: a smart economy, smart mobility, a smart environment, smart people, smart living, smart governance.</span></p>
    <p>In my mind, being a “smart city” encompasses a lot of things – incorporating technology, yes, but also with an eye on cultural and aspects. At the end of the day, we all want to work, live, play and visit places that are safe, beautiful and clean, (maybe even exciting and invigorating), and we want to get stuff done expediently and with less stress. Being “smart” is a tool to help accomplish these goals. And, being smart means connecting the dots to bring out the best of all these facets!<br>Through three Key Topics, the 2020 Ravteq Forum explores how the built environment connects the dots to achieve these goals.</p>
  </div>

  <svg class="abs" style="left:0;top:700px" width="540" height="66" aria-hidden="true"><ellipse cx="274" cy="100" rx="245" ry="90" fill="var(--green)"/></svg>
  <div class="abs footer-url" style="left:8px">ravteqforum.org</div>
</section>

</body>
</html>
```